Permanent Makeup (cosmetics salon) Brochure

We need a 2-4 sites brochure for our Permanent Makeup (cosmetics salon). Our company is based in Austria / Vienna. -> Our homepage is www.mk-lorenzhuber.at
This brochure should show which treatments we provide ot our customers.

I've uploaded our old brochure, the content (text) would be nearly the same (look form "Must Haves", pics have to be new (look uploaded pics)
The old brochure is to dark. -> look for our homepage maybe you can make it like this

Target Market(s)

woman, age 25-70 years who wants to have permanent makeup on eyebrows, lips or eyeliner

Industry/Entity Type

Beauty Salon

Requirements
Must have
• pics which are uploaded.

*This text (somithing about our business)
"Für Frau Lorenzhuber ist Permanent Makeup ein Kunsthandwerk. Das Team von MK-Lorenzhuber ist spezialisiert auf natürliches Permanent Makeup damit der individuelle Typ jeder Kundin am schönsten zum Ausdruck kommt."

*We do this treatments: (english)
+ Augenbrauen Microblading (eyebrows)
+ Augenbrauen Permanent Makeup (eyebrows2)
+ Lidstrich Permanent Makeup (eyeliner)
+ Lip Blushing (lips)
+ Lippen Permanent Makeup (lips2)

* Our addresses (2 locations)
Wien
Kerngasse 7b/12, 1010 Wien
Tel: 01/5827316

Villach
Birkenhofweg 24, 9524 St. Ulrich
Tel: 0676/3158940

Mail: info@mk-lorenzhuber.at
www.mk-lorenzhuber.at

```html
<!DOCTYPE html>
<html lang="de">
<head>
<meta charset="utf-8">
<title>Maja Lorenzhuber – Kosmetikstudio Broschüre</title>
<link rel="stylesheet" href="https://fonts.googleapis.com/css2?family=Josefin+Sans:wght@300;400&family=Lato:wght@400;700&family=Oswald:wght@200&display=swap">
<style>
  :root{
    --navy:#2a3250;
    --navy-soft:#4a556e;
    --gold:#e8c35a;
    --gold-deep:#d3a43a;
    --paper:#f1f1f2;
    --mist:#e4e5e8;
    --ink:#3b3d46;
    --stage:#dcdcde;
    --white:#ffffff;
  }
  *{margin:0;padding:0;box-sizing:border-box}
  html,body{width:1200px;height:1129px;overflow:hidden;background:var(--stage)}
  body{position:relative;font-family:"Josefin Sans",sans-serif;color:var(--ink)}
  .spread{position:absolute;left:240px;width:804px;height:403px;background:var(--paper);overflow:hidden}
  .spread--outer{top:150px}
  .spread--inner{top:586px}
  .spread__art{position:absolute;inset:0;width:804px;height:403px}
  .abs{position:absolute}
  .center{text-align:center}

  /* brand line */
  .brand{display:flex;align-items:center;justify-content:center;gap:7px;font-family:"Josefin Sans",sans-serif;font-weight:300;letter-spacing:.5px;white-space:nowrap}
  .brand__dot{border:2px solid var(--gold);border-radius:50%;flex:none}
  .brand--light{color:var(--white)}
  .brand--dark{color:var(--ink)}
  .brand-sub{font-family:"Lato",sans-serif;font-size:5.5px;letter-spacing:2.6px;color:var(--white)}
  .tagline{font-family:"Lato",sans-serif;font-weight:700;font-size:5.6px;letter-spacing:.4px;color:var(--ink)}

  /* cover */
  .cover-intro{left:50px;top:117px;width:302px;font-weight:300;font-size:12.4px;line-height:16.6px;color:var(--gold)}
  .location{top:327px;font-family:"Lato",sans-serif}
  .location__name{font-size:8.4px;color:var(--gold);margin-bottom:3px;font-family:"Josefin Sans",sans-serif}
  .location__line{display:flex;align-items:center;gap:4px;font-size:7px;line-height:10.4px;color:var(--ink)}
  .location__line svg{width:6px;height:6px;flex:none}
  .location-divider{left:196px;top:316px;width:1px;height:64px;background:#cfd0d4}

  .claim{left:640px;top:100px;width:134px;color:var(--white)}
  .claim__big{font-family:"Oswald",sans-serif;font-weight:200;font-size:33px;line-height:40px;letter-spacing:.5px}
  .claim__small{font-weight:300;font-size:14.5px;letter-spacing:1.4px;line-height:18px}
  .claim__von{display:flex;align-items:center;justify-content:center;gap:8px;font-weight:300;font-size:15px;letter-spacing:1.4px;margin-top:6px}
  .claim__von span.rule{width:30px;height:1px;background:var(--gold)}
  .claim__innen{font-weight:300;font-size:26px;letter-spacing:2.6px;line-height:26px}
  .web-pill{display:block;margin:8px auto 0;width:110px;height:11px;border-radius:6px;background:var(--gold);font-family:"Lato",sans-serif;font-size:6px;line-height:11px;color:var(--white)}

  /* inner */
  .about-title{left:0;top:249px;width:402px;font-weight:300;font-size:13.4px;letter-spacing:.3px;color:var(--gold)}
  .about-copy{left:25px;top:279px;width:352px;font-weight:300;font-size:11.2px;line-height:18.8px;color:var(--ink)}
  .booking{top:366px;height:22px;width:402px;display:flex;align-items:center;justify-content:center;gap:7px;font-weight:300;font-size:11.2px;color:var(--white)}
  .booking--left{left:0;background:var(--navy-soft)}
  .booking--right{left:402px;background:var(--navy)}
  .booking__url{color:var(--gold)}
  .booking__dot{width:7px;height:7px;border:1.5px solid var(--gold);border-radius:50%}

  .section-title{left:424px;top:91px;width:360px;display:flex;align-items:center;justify-content:center;gap:14px;font-weight:300;font-size:13px;color:var(--gold);letter-spacing:.2px}
  .section-title .rule{width:56px;height:1px;background:var(--gold)}
  .treatment{position:absolute;width:120px;text-align:center}
  .treatment__photo{display:block;margin:0 auto;width:92px;height:73px;border-right:1.5px solid var(--gold);border-bottom:1.5px solid var(--gold)}
  .treatment__label{margin-top:9px;font-weight:300;font-size:9.6px;line-height:13px;letter-spacing:.3px;color:var(--ink)}
  .tone-brow{background:linear-gradient(160deg,#c49a82,#e8c6b2 55%,#d9b29b)}
  .tone-brow2{background:linear-gradient(160deg,#b98f78,#e2bea8 55%,#cfa48c)}
  .tone-eye{background:linear-gradient(160deg,#cbb0a6,#e6d3cc 55%,#9fb8b4)}
  .tone-lip{background:linear-gradient(180deg,#e7c3b4,#e59a92 45%,#eab3a8)}
  .tone-lip2{background:linear-gradient(180deg,#f0d6cb,#e48f86 50%,#f1d0c5)}
</style>
</head>
<body>

<!-- Outer spread: back + cover -->
<section class="spread spread--outer">
  <svg class="spread__art" viewBox="0 0 804 403" aria-hidden="false">
    <defs>
      <linearGradient id="navyFade" x1="0" y1="0" x2="0" y2="1">
        <stop offset="0" stop-color="#2a3250"/>
        <stop offset="1" stop-color="#4b566c"/>
      </linearGradient>
      <linearGradient id="navyCover" x1="0" y1="0" x2="0" y2="1">
        <stop offset="0" stop-color="#2f3858"/>
        <stop offset="1" stop-color="#3f4a66"/>
      </linearGradient>
      <linearGradient id="skinFace" x1="0" y1="0" x2="1" y2="1">
        <stop offset="0" stop-color="#6b4a3c"/>
        <stop offset=".35" stop-color="#d9a88c"/>
        <stop offset=".7" stop-color="#c98f74"/>
        <stop offset="1" stop-color="#7f8fa0"/>
      </linearGradient>
      <linearGradient id="goldSheen" x1="0" y1="0" x2="1" y2="0">
        <stop offset="0" stop-color="#d3a43a"/>
        <stop offset=".5" stop-color="#f2d77c"/>
        <stop offset="1" stop-color="#d3a43a"/>
      </linearGradient>
      <radialGradient id="eyeGreen"><stop offset="0" stop-color="#dcc3b8"/><stop offset="1" stop-color="#b9a39a"/></radialGradient>
      <radialGradient id="lipPink"><stop offset="0" stop-color="#e99c92"/><stop offset="1" stop-color="#e4bcae"/></radialGradient>
      <radialGradient id="eyeBrown"><stop offset="0" stop-color="#d6ab93"/><stop offset="1" stop-color="#b88a72"/></radialGradient>
    </defs>
    <!-- back page -->
    <rect x="0" y="0" width="402" height="403" fill="url(#navyFade)"/>
    <path d="M0,256 C70,228 140,222 200,224 L200,403 L0,403 Z" fill="url(#goldSheen)"/>
    <path d="M0,304 C70,264 140,246 200,240 C280,240 340,268 402,280 L402,403 L0,403 Z" fill="var(--mist)"/>
    <!-- cover page -->
    <rect x="402" y="0" width="402" height="403" fill="url(#navyCover)"/>
    <rect x="402" y="0" width="234" height="330" fill="url(#skinFace)" role="img" aria-label="Porträtfoto einer Frau mit makelloser Haut, Hand am Kinn"/>
    <path d="M560,314 C650,318 740,298 804,262 L804,292 C760,304 700,317 620,318 Z" fill="url(#goldSheen)"/>
    <path d="M402,282 C480,300 540,318 620,318 C700,317 760,304 804,292 L804,403 L402,403 Z" fill="var(--mist)"/>
    <!-- treatment circles -->
    <circle cx="113" cy="241" r="43" fill="url(#eyeGreen)" stroke="var(--gold)" stroke-width="2.5" role="img" aria-label="Nahaufnahme eines grünen Auges mit Lidstrich"/>
    <circle cx="286" cy="241" r="42" fill="url(#eyeBrown)" stroke="var(--gold)" stroke-width="2.5" role="img" aria-label="Nahaufnahme eines braunen Auges mit Augenbraue"/>
    <circle cx="198" cy="243" r="53" fill="url(#lipPink)" stroke="var(--gold)" stroke-width="3" role="img" aria-label="Nahaufnahme voller Lippen nach Lip Blushing"/>
  </svg>

  <div class="abs center" style="left:0;top:58px;width:402px">
    <div class="brand brand--light" style="font-size:17px"><span class="brand__dot" style="width:18px;height:18px"></span>Maja Lorenzhuber</div>
    <div class="brand-sub" style="margin-top:9px">KOSMETIKSTUDIO</div>
  </div>

  <p class="abs center cover-intro">Ihr Kosmetikstudio und Beauty Salon in 1010 Wien Professionelles Microblading und Permanent Make Up für gehobene Ansprüche</p>

  <div class="abs location" style="left:62px">
    <div class="location__name">WIEN</div>
    <div class="location__line"><svg viewBox="0 0 10 10"><path d="M5 0a3.4 3.4 0 0 0-3.4 3.4C1.6 6 5 10 5 10s3.4-4 3.4-6.6A3.4 3.4 0 0 0 5 0zm0 4.8a1.4 1.4 0 1 1 0-2.8 1.4 1.4 0 0 1 0 2.8z" fill="#3b3d46"/></svg>Kerngasse 7b/12, 1010 Wien</div>
    <div class="location__line"><svg viewBox="0 0 10 10"><path d="M2 0.5l2 2-1 1.3c.6 1.3 1.6 2.3 2.9 2.9L7.2 5.7l2 2-1.3 1.6C4.6 9.2 0.8 5.4 0.6 2z" fill="#3b3d46"/></svg>01/5827316</div>
    <div class="location__line"><svg viewBox="0 0 10 10"><path d="M0.8 4.5L5 1.5l4.2 3V9H.8z" fill="none" stroke="#3b3d46"/></svg>info@mk-lorenzhuber.at</div>
  </div>
  <div class="abs location-divider"></div>
  <div class="abs location" style="left:233px">
    <div class="location__name">VILLACH</div>
    <div class="location__line"><svg viewBox="0 0 10 10"><path d="M5 0a3.4 3.4 0 0 0-3.4 3.4C1.6 6 5 10 5 10s3.4-4 3.4-6.6A3.4 3.4 0 0 0 5 0zm0 4.8a1.4 1.4 0 1 1 0-2.8 1.4 1.4 0 0 1 0 2.8z" fill="#3b3d46"/></svg>Birkenhofweg 24, 9524 St. Ulrich</div>
    <div class="location__line"><svg viewBox="0 0 10 10"><path d="M2 0.5l2 2-1 1.3c.6 1.3 1.6 2.3 2.9 2.9L7.2 5.7l2 2-1.3 1.6C4.6 9.2 0.8 5.4 0.6 2z" fill="#3b3d46"/></svg>0676/3158940</div>
    <div class="location__line"><svg viewBox="0 0 10 10"><path d="M0.8 4.5L5 1.5l4.2 3V9H.8z" fill="none" stroke="#3b3d46"/></svg>info@mk-lorenzhuber.at</div>
  </div>

  <div class="abs claim center">
    <div class="claim__big">SCHÖNHEIT</div>
    <div class="claim__small">kommt nicht nur</div>
    <div class="claim__von"><span class="rule"></span>von<span class="rule"></span></div>
    <div class="claim__innen">innen</div>
    <span class="web-pill">www.mk-lorenzhuber.at</span>
  </div>

  <div class="abs center" style="left:402px;top:340px;width:402px">
    <div class="brand brand--dark" style="font-size:17px"><span class="brand__dot" style="width:20px;height:20px"></span>Maja Lorenzhuber</div>
    <div class="tagline" style="margin-top:7px">WAS IHNEN WERTVOLL IST, GEHÖRT IN GUTE HÄNDE</div>
  </div>
</section>

<!-- Inner spread: about + treatments -->
<section class="spread spread--inner">
  <svg class="spread__art" viewBox="0 0 804 403">
    <defs>
      <linearGradient id="skinClose" x1="0" y1="0" x2="1" y2="0">
        <stop offset="0" stop-color="#e7c2a9"/>
        <stop offset=".45" stop-color="#d9a58c"/>
        <stop offset="1" stop-color="#eed6c0"/>
      </linearGradient>
      <linearGradient id="goldArc" x1="0" y1="1" x2="1" y2="0">
        <stop offset="0" stop-color="#d3a43a"/>
        <stop offset=".6" stop-color="#f2d77c"/>
        <stop offset="1" stop-color="#d3a43a"/>
      </linearGradient>
      <linearGradient id="pageShade" x1="0" y1="0" x2="1" y2="0">
        <stop offset="0" stop-color="#d6d7da"/>
        <stop offset="1" stop-color="#f1f1f2" stop-opacity="0"/>
      </linearGradient>
    </defs>
    <path d="M0,0 L372,0 C370,110 250,214 0,225 Z" fill="url(#skinClose)" role="img" aria-label="Nahaufnahme eines Frauenauges mit Permanent Makeup an Augenbraue und Lidstrich"/>
    <path d="M0,232 C270,222 382,110 382,0" fill="none" stroke="url(#goldArc)" stroke-width="3"/>
    <rect x="402" y="0" width="28" height="403" fill="url(#pageShade)"/>
  </svg>

  <div class="abs center" style="left:310px;top:102px;width:84px;height:84px;border:5px solid var(--gold);border-radius:50%;display:flex;align-items:center;justify-content:center;font-weight:300;font-size:8px;line-height:10px;color:var(--white)">Maja<br>Lorenzhuber</div>

  <h2 class="abs center about-title" style="font-weight:300">IHR KOSMETIKSTUDIO UND BEAUTY SALON</h2>
  <p class="abs center about-copy">Für Frau Lorenzhuber ist Permanent Makeup ein Kunsthandwerk. Das Team von MK-Lorenzhuber ist spezialisiert auf natürliches Permanent Makeup damit der individuelle Typ jeder Kundin am schönsten zum Ausdruck kommt.</p>

  <div class="abs center" style="left:402px;top:32px;width:402px">
    <div class="brand brand--dark" style="font-size:17px"><span class="brand__dot" style="width:20px;height:20px"></span>Maja Lorenzhuber</div>
    <div class="tagline" style="margin-top:7px">WAS IHNEN WERTVOLL IST, GEHÖRT IN GUTE HÄNDE</div>
  </div>

  <h2 class="abs section-title" style="font-weight:300"><span class="rule"></span>WE DO THIS TREATMENTS<span class="rule"></span></h2>

  <div class="treatment" style="left:415px;top:126px"><span class="treatment__photo tone-brow" role="img" aria-label="Augenbraue nach Microblading"></span><p class="treatment__label">Augenbrauen Microblading<br>(eyebrows)</p></div>
  <div class="treatment" style="left:547px;top:126px"><span class="treatment__photo tone-brow2" role="img" aria-label="Augenbraue mit Permanent Makeup"></span><p class="treatment__label">Augenbrauen Permanent<br>Makeup (eyebrows2)</p></div>
  <div class="treatment" style="left:679px;top:126px"><span class="treatment__photo tone-eye" role="img" aria-label="Auge mit Permanent Lidstrich"></span><p class="treatment__label">Lidstrich Permanent<br>Makeup (eyeliner)</p></div>
  <div class="treatment" style="left:479px;top:244px"><span class="treatment__photo tone-lip" role="img" aria-label="Lippen nach Lip Blushing"></span><p class="treatment__label">Lip Blushing<br>(lips)</p></div>
  <div class="treatment" style="left:617px;top:244px"><span class="treatment__photo tone-lip2" role="img" aria-label="Lippen mit Permanent Makeup"></span><p class="treatment__label">Lippen Permanent<br>Makeup (lips2)</p></div>

  <div class="abs booking booking--left">Online Termin vereinbaren <span class="booking__dot"></span> <span class="booking__url">www.mk-lorenzhuber.at</span></div>
  <div class="abs booking booking--right">Online Termin vereinbaren <span class="booking__dot"></span> <span class="booking__url">www.mk-lorenzhuber.at</span></div>
</section>

</body>
</html>
```